Oak Fitness postcard

*my business is a fitness business. I offer at home personal fitness training. I don't own a gym, I go house to house training people.
*I would like the flyer to have a colorful enviroment with a picture of a happy and fit woman, because women are my target market. Mabey have her excersing or being trained by a male fitness trainer.
*For the headline, I don't want the title of my business, instead I want an exciting headline. Something mabey like "fit in the the jeans you love" anything that says the client could lose weight
*for the services please add- training at your home. Meal plans based on foods you love. Educate you of proper dieting and nutrition. High protein dieting
*for benifits please add- reduce cellulite. Rdeuce stretch marks. Lose Permanente weight. Flatten and tone stomach. Sleep better.
*I am offering 1 full free training session with no obligation, please put that in big bold letters
*please make the before and after pic blend into the design and add the testimonial "Losing weight felt impossible till I went on a high protein diet, then the pounds dropped rapidly." Melissa T from Boston MS.
*on top of the before and after pic, please add "proof that high protein diets work"
*in big bold letters at the bottom or center please add a call to action saying something like "CALL 731-558-3094 and ask about my free training session"
*at bottom of flyer my contact info is "derek Holloway (certified personal trainer and nutritional specialist)" and phone number "731-558-3094" business name "oak fitness"

Industry/Entity Type

Business

```html
<!DOCTYPE html>
<html lang="en">
<head>
<meta charset="utf-8">
<title>Oak Fitness Postcard</title>
<link href="https://fonts.googleapis.com/css2?family=Bebas+Neue&family=Oswald:wght@400;500;600;700&display=swap" rel="stylesheet">
<style>
  :root {
    --violet-deep: #4b1f86;
    --violet: #7a35b0;
    --magenta: #c44bb8;
    --headline: #c99ad6;
    --burst: #c582cc;
    --ink-dark: #321457;
    --frame: #4a2380;
    --bar: #5b2a8f;
    --yellow: #f6ea5c;
    --white: #ffffff;
  }
  * { box-sizing: border-box; margin: 0; padding: 0; }
  html, body { width: 1200px; height: 930px; overflow: hidden; }
  body { font-family: "Oswald", "Arial Narrow", sans-serif; }

  .postcard {
    position: relative;
    width: 1200px;
    height: 930px;
    overflow: hidden;
    background:
      linear-gradient(128deg, transparent 0 48%, rgba(255,255,255,0.08) 48% 62%, transparent 62%),
      linear-gradient(150deg, transparent 0 70%, rgba(255,255,255,0.06) 70% 80%, transparent 80%),
      radial-gradient(ellipse at 15% 95%, rgba(230,110,210,0.75), transparent 55%),
      radial-gradient(ellipse at 85% 20%, rgba(170,80,200,0.55), transparent 60%),
      linear-gradient(160deg, var(--violet-deep) 0%, var(--violet) 45%, var(--magenta) 100%);
  }

  .headline {
    position: absolute;
    top: 18px;
    left: 0;
    width: 1200px;
    text-align: center;
    font-family: "Bebas Neue", "Oswald", sans-serif;
    font-size: 114px;
    line-height: 1;
    letter-spacing: 1px;
    color: var(--headline);
    opacity: 0.92;
  }

  .hero-frame {
    position: absolute;
    left: 34px;
    top: 189px;
    width: 720px;
    height: 548px;
    background: var(--frame);
    border-radius: 6px;
    padding: 11px;
  }
  .hero-photo {
    width: 100%;
    height: 100%;
    background:
      radial-gradient(ellipse at 70% 40%, #b9a7a0, transparent 60%),
      linear-gradient(135deg, #6d6a72 0%, #9a8e88 45%, #3a3640 100%);
  }

  .offer-burst {
    position: absolute;
    left: 106px;
    top: 122px;
    width: 268px;
    height: 268px;
  }
  .offer-burst svg { position: absolute; inset: 0; }
  .offer-text {
    position: absolute;
    inset: 0;
    display: flex;
    flex-direction: column;
    justify-content: center;
    align-items: center;
    text-align: center;
    font-weight: 600;
    color: var(--ink-dark);
    font-size: 30px;
    line-height: 1;
    text-transform: uppercase;
    padding-bottom: 14px;
  }
  .offer-text .big { font-size: 44px; }

  .call-to-action {
    position: absolute;
    left: 34px;
    top: 746px;
    width: 720px;
    text-align: center;
    color: var(--white);
    text-transform: uppercase;
    line-height: 1;
  }
  .call-to-action .cta-main {
    display: block;
    font-family: "Bebas Neue", "Oswald", sans-serif;
    font-size: 58px;
    letter-spacing: 1px;
  }
  .call-to-action .cta-main em {
    font-style: normal;
    color: var(--yellow);
  }
  .call-to-action .cta-sub {
    display: block;
    font-weight: 700;
    font-size: 24px;
    margin-top: 2px;
  }

  .benefits {
    position: absolute;
    right: 38px;
    top: 136px;
    text-align: right;
    color: var(--white);
  }
  .benefits h2 {
    font-weight: 600;
    font-size: 40px;
    line-height: 1;
    color: var(--yellow);
    letter-spacing: 1px;
    margin-bottom: 3px;
  }
  .benefits ul { list-style: none; }
  .benefits li {
    font-weight: 500;
    font-size: 25px;
    line-height: 29.5px;
    letter-spacing: -0.3px;
  }

  .proof-label {
    position: absolute;
    left: 876px;
    top: 480px;
    font-size: 12px;
    color: var(--white);
  }

  .result-photo {
    position: absolute;
    background: var(--white);
    padding: 5px;
    box-shadow: 0 3px 8px rgba(40,0,60,0.35);
  }
  .result-photo div { width: 100%; height: 100%; }
  .result-before { left: 835px; top: 515px; width: 110px; height: 232px; }
  .result-before div { background: linear-gradient(180deg, #c9a58a, #a58aa8 60%, #7a8fb0); }
  .result-after { left: 922px; top: 508px; width: 138px; height: 246px; transform: rotate(4deg); }
  .result-after div { background: linear-gradient(180deg, #d8d2c8, #8d7f76 55%, #3c3438); }

  .testimonial {
    position: absolute;
    left: 834px;
    top: 760px;
    width: 200px;
    color: var(--white);
    font-style: italic;
    font-size: 16.5px;
    line-height: 21px;
    letter-spacing: -0.3px;
  }
  .testimonial cite {
    display: block;
    text-align: right;
    font-size: 9px;
    line-height: 1;
    margin-top: 7px;
    font-style: normal;
  }

  .contact-bar {
    position: absolute;
    left: 76px;
    top: 862px;
    width: 1048px;
    height: 80px;
    background: var(--bar);
    border-radius: 38px 38px 0 0;
    display: flex;
    justify-content: center;
    align-items: flex-start;
    padding-top: 17px;
    gap: 10px;
    color: var(--white);
    font-size: 23px;
    line-height: 1;
    letter-spacing: -0.4px;
  }
  .contact-bar .phone-icon {
    width: 30px;
    height: 30px;
    background: var(--white);
    border-radius: 6px;
    display: flex;
    align-items: center;
    justify-content: center;
    margin-top: -3px;
  }
</style>
</head>
<body>
<main class="postcard">
  <h1 class="headline">Fit in the jeans you love</h1>

  <div class="hero-frame">
    <div class="hero-photo" role="img" aria-label="Fit woman exercising in a gym, guided by a male personal trainer"></div>
  </div>

  <div class="offer-burst">
    <svg viewBox="0 0 268 268" aria-hidden="true">
      <polygon fill="var(--burst)" points="134,0 148,32 172,6 176,40 207,20 200,54 236,44 218,74 254,76 226,98 262,110 230,126 264,144 230,156 254,182 218,182 236,214 200,210 208,244 176,226 172,262 148,236 134,268 120,236 96,262 92,226 60,244 68,210 32,214 50,182 14,182 38,156 4,144 38,126 6,110 42,98 14,76 50,74 32,44 68,54 60,20 92,40 96,6 120,32"/>
    </svg>
    <div class="offer-text">
      <span><span class="big">1</span> Full free</span>
      <span>Training session</span>
      <span>With no</span>
      <span>Obligation</span>
    </div>
  </div>

  <p class="call-to-action">
    <span class="cta-main">Call <em>731-558-3094</em></span>
    <span class="cta-sub">and ask about my free training session</span>
  </p>

  <section class="benefits">
    <h2>BENEFITS</h2>
    <ul>
      <li>Training at your home</li>
      <li>Meal plans based on foods you love</li>
      <li>Educate you of proper dieting<br>and nutrition</li>
      <li>High protein dieting</li>
      <li>Reduce cellulite</li>
      <li>Reduce stretch marks</li>
      <li>Lose Permanente weight.</li>
      <li>Flatten and tone stomach</li>
      <li>Sleep better</li>
    </ul>
  </section>

  <p class="proof-label">proof that high protein diets work</p>

  <div class="result-photo result-before"><div role="img" aria-label="Client before photo"></div></div>
  <div class="result-photo result-after"><div role="img" aria-label="Client after photo"></div></div>

  <blockquote class="testimonial">
    <p>"Losing weight felt impossible till I went on a high protein diet, then the pounds dropped rapidly."</p>
    <cite>Melissa T from Boston MS</cite>
  </blockquote>

  <footer class="contact-bar">
    <span>DEREK HOLLOWAY - Certified personal trainer and nutritional specialist -</span>
    <span class="phone-icon">
      <svg width="20" height="20" viewBox="0 0 24 24" aria-hidden="true">
        <path fill="var(--bar)" d="M6.6 10.8a15.1 15.1 0 0 0 6.6 6.6l2.2-2.2c.3-.3.7-.4 1-.2 1.1.4 2.3.6 3.6.6.6 0 1 .4 1 1V20c0 .6-.4 1-1 1A17 17 0 0 1 3 4c0-.6.4-1 1-1h3.5c.6 0 1 .4 1 1 0 1.3.2 2.5.6 3.6.1.3 0 .7-.2 1z"/>
      </svg>
    </span>
    <span>731-558-3094 - oak fitness</span>
  </footer>
</main>
</body>
</html>
```